Collaborative Law Bus Stop Bench Design

We are looking for a design for a bus stop bench-the size is 74 inches in length and 22 inches wide.We are a group of family law lawyers, social workers and accountants who are committed to resolving marital breakdowns without going to court.
As this is a bus stop ad not a lot of words can be used.
The sign needs to show our website www.tidewellhomecounsel.com prominently
We want the design to focus on the advantages of our process ie. not going to court-like"Don't air your dirty laundry"-a design with a clothesline or something like that.
It needs to be clear and uncomplicated but memorable.

```html
<!DOCTYPE html>
<html lang="en">
<head>
<meta charset="utf-8">
<title>Why Create a Public Drama? – Bus Stop Bench</title>
<link rel="stylesheet" href="https://fonts.googleapis.com/css2?family=Arimo:wght@700&display=swap">
<style>
  :root {
    --page-white: #ffffff;
    --backdrop-red: #b8160c;
    --panel-black: #1b1b1b;
    --text-white: #ffffff;
    --text-gold: #f2b31c;
  }
  html, body {
    margin: 0;
    padding: 0;
    width: 1200px;
    height: 900px;
    overflow: hidden;
    background: var(--page-white);
  }
  .canvas {
    position: relative;
    width: 1200px;
    height: 900px;
    background: var(--page-white);
    font-family: "Arimo", Arial, Helvetica, sans-serif;
  }
  .bench-banner {
    position: absolute;
    left: 0;
    top: 271px;
    width: 1200px;
    height: 356px;
  }
  .stage-backdrop {
    position: absolute;
    inset: 0;
    background: var(--backdrop-red);
  }
  .message-panel {
    position: absolute;
    left: 180px;
    top: 43px;
    width: 840px;
    height: 211px;
    background: var(--panel-black);
    text-align: center;
  }
  .headline,
  .subline,
  .web-address {
    position: absolute;
    left: 0;
    right: 0;
    margin: 0;
    font-weight: 700;
    white-space: nowrap;
  }
  .headline {
    top: 33px;
    font-size: 48px;
    line-height: 54px;
    color: var(--text-white);
  }
  .subline {
    top: 86px;
    font-size: 37px;
    line-height: 42px;
    color: var(--text-gold);
  }
  .web-address {
    top: 149px;
    font-size: 35px;
    line-height: 40px;
    color: var(--text-white);
  }
</style>
</head>
<body>
  <div class="canvas">
    <section class="bench-banner">
      <div class="stage-backdrop" role="img" aria-label="Photograph of a red theatre stage curtain above a wooden stage floor"></div>
      <div class="message-panel">
        <h1 class="headline">WHY CREATE A PUBLIC DRAMA?</h1>
        <p class="subline">Settle Marital Disputes Without Courts.</p>
        <p class="web-address">www.tidewellhomecounsel.com</p>
      </div>
    </section>
  </div>
</body>
</html>
```